Kelekeleoliolimaiwaipeleke Fish Package

We need a package design for our Kelekeleoliolimaiwaipeleke Fish (not Bravlin fish). We plan to sell them at Hawaii stores to start and them take them to the mainland. We are looking for a package design that includes the front with a Kelekeleoliolimaiwaipeleke Fish (not a photo) and a back design with a photo of the fish (we will supply), information about the fish and nutrition information.

Target Market(s)

Premium market

Colors

Designer to choose colors to be used in the design.

Requirements
Must have
• See attached overview - also, it must include our logo (which we will provide)
Nice to have
• See attached overview

```html
<!DOCTYPE html>
<html lang="en">
<head>
<meta charset="utf-8">
<title>Kelekeleoliolimaiwaipeleke Fish Package</title>
<link rel="stylesheet" href="https://fonts.googleapis.com/css2?family=Lilita+One&family=Righteous&display=swap">
<style>
  :root {
    --backdrop: #63628a;
    --pouch-top: #f4dde9;
    --pouch-bottom: #fbeef4;
    --brand-coral: #e84a6a;
    --plum: #7a2a5f;
    --plum-deep: #5e2350;
    --violet: #6a4f86;
    --teal: #7fb0c0;
    --mauve: #a17fa8;
    --pink: #e27aa6;
    --aqua: #a9dfe4;
    --white: #ffffff;
  }
  * { margin: 0; padding: 0; box-sizing: border-box; }
  html, body {
    width: 1147px;
    height: 1200px;
    overflow: hidden;
    background: var(--backdrop);
  }
  .pouch {
    position: absolute;
    left: 145px;
    top: 95px;
    width: 855px;
    height: 1031px;
    background: linear-gradient(180deg, var(--pouch-top) 0%, var(--pouch-bottom) 60%, var(--white) 100%);
    box-shadow: 0 4px 14px rgba(30, 28, 60, 0.45);
    overflow: hidden;
  }
  .pouch-art { position: absolute; inset: 0; width: 855px; height: 1031px; }
  .brand-name {
    font-family: "Righteous", sans-serif;
    font-size: 92px;
    letter-spacing: 4px;
    fill: var(--brand-coral);
  }
  .species-arc {
    font-family: "Lilita One", sans-serif;
    font-size: 62px;
    stroke: var(--white);
    stroke-width: 3px;
    paint-order: stroke;
  }
  .label-line {
    font-family: "Lilita One", sans-serif;
    paint-order: stroke;
    stroke: var(--plum);
    stroke-linejoin: round;
  }
  .label-premium { font-size: 52px; fill: var(--white); stroke-width: 9px; }
  .label-species { font-size: 33px; fill: var(--white); stroke-width: 7px; }
  .label-treat { font-size: 76px; stroke-width: 11px; }
  .label-flavour, .label-weight {
    font-family: "Lilita One", sans-serif;
    fill: var(--violet);
    stroke: var(--white);
    stroke-width: 5px;
    paint-order: stroke;
    letter-spacing: 1px;
  }
  .label-flavour { font-size: 28px; }
  .label-weight { font-size: 26px; }
</style>
</head>
<body>
  <div class="pouch">
    <svg class="pouch-art" viewBox="0 0 855 1031" xmlns="http://www.w3.org/2000/svg">
      <defs>
        <linearGradient id="arcInk" x1="0" y1="0" x2="1" y2="0">
          <stop offset="0" stop-color="#6b3a78"/>
          <stop offset="0.45" stop-color="#6fa4b8"/>
          <stop offset="1" stop-color="#a782ad"/>
        </linearGradient>
        <linearGradient id="treatInk" x1="0" y1="0" x2="0" y2="1">
          <stop offset="0.2" stop-color="#ffffff"/>
          <stop offset="1" stop-color="#9fd9e2"/>
        </linearGradient>
        <linearGradient id="flavourInk" x1="0" y1="0" x2="1" y2="0">
          <stop offset="0" stop-color="#5f5a8a"/>
          <stop offset="1" stop-color="#b04c8e"/>
        </linearGradient>
        <linearGradient id="wavesTone" x1="0" y1="0" x2="1" y2="1">
          <stop offset="0" stop-color="#eba3c6" stop-opacity="0.55"/>
          <stop offset="0.45" stop-color="#8fbfcc" stop-opacity="0.65"/>
          <stop offset="1" stop-color="#e892bd" stop-opacity="0.6"/>
        </linearGradient>
        <linearGradient id="fishTone" x1="0" y1="0" x2="1" y2="1">
          <stop offset="0" stop-color="#d6a574"/>
          <stop offset="0.6" stop-color="#3a4f9a"/>
          <stop offset="1" stop-color="#c99a6c"/>
        </linearGradient>
        <path id="speciesCurve" d="M 106 640 A 327 327 0 0 1 760 640"/>
      </defs>

      <!-- hanger slot -->
      <rect class="hanger-slot" x="360" y="58" width="140" height="44" rx="14" fill="var(--backdrop)"/>

      <!-- lower wave backdrop -->
      <path class="wave-field" role="img" aria-label="Abstract flowing pink and teal waves and bubbles"
            d="M0 600 C 140 560 260 640 420 600 C 560 565 700 560 855 600 L 855 1031 L 0 1031 Z"
            fill="url(#wavesTone)"/>

      <!-- island map -->
      <rect class="island-map" role="img" aria-label="Illustrated map of the Hawaiian islands"
            x="360" y="350" width="330" height="160" rx="40" fill="#7f9be0" opacity="0.55"/>

      <!-- fish illustration -->
      <rect class="fish-illustration" role="img" aria-label="Watercolour illustration of the Kelekeleoliolimaiwaipeleke fish"
            x="182" y="420" width="432" height="212" rx="100" fill="url(#fishTone)" opacity="0.85"/>

      <text class="brand-name" x="427" y="220" text-anchor="middle">KAI ONO</text>

      <text class="species-arc" fill="url(#arcInk)">
        <textPath href="#speciesCurve" startOffset="50%" text-anchor="middle" textLength="1000" lengthAdjust="spacingAndGlyphs">KELEKELEOLIOLIMAIWAIPELEKE</textPath>
      </text>

      <text class="label-line label-premium" x="427" y="733" text-anchor="middle">Premium</text>
      <text class="label-line label-species" x="427" y="786" text-anchor="middle">Kelekeleoliolimaiwaipeleke Fish</text>
      <text class="label-line label-treat" x="427" y="855" text-anchor="middle" fill="url(#treatInk)">Hawaiian Treat</text>
      <text class="label-flavour" x="427" y="933" text-anchor="middle" fill="url(#flavourInk)">PINEAPPLE, CITRUS AND RASPBERRY</text>
      <text class="label-weight" x="427" y="988" text-anchor="middle" fill="url(#flavourInk)">NET WEIGHT 8.0 OZ</text>
    </svg>
  </div>
</body>
</html>
```